Learn-to-Swim Program for Children's Day Camp (Walter Brightley Fieldgrounds)

We are a children's camp with a robust swim instruction program and we need a series of 5 kid-friendly banners which list the skills learned in our swim program that can be hung up around each outdoor pool complex. All together there are 6 overarching levels and 12 sublevels (see attached). Except for the Level V & VI, each banner should be one overarching level and the 2-3 sublevels that define it.

Each swim level has a name, most of which are sea creatures, and we want to have a corresponding image/avatar to go with the swim level name (e.g. tadpole, barracuda, orca, goldfish, catfish).

The banners should be 3 feet (width) by 5 feet (height). The banners will be hung outdoors so it needs a color scheme that won't get lost in the sunlight.

We will want to include our logo but do not need the design to match our logo colors. Logo can be in black or white.

Our website is: www.campwbf.example

Target Market(s)

children age 5 - 12

Industry/Entity Type

children's day camp

Requirements
Must have
• A progression from level I to level VI. Should have a happy, bright, fun, tone, text MUST be legible from at least a 5 foot distance
Should not have
• adult themes, a scheme that evokes sadness or fear

```html
<!DOCTYPE html>
<html lang="en">
<head>
<meta charset="utf-8">
<title>Arc I – Wader &amp; Splasher</title>
<link rel="stylesheet" href="https://fonts.googleapis.com/css2?family=Fredoka:wght@600;700&family=Fira+Sans:wght@500&family=Fira+Sans+Condensed:wght@600&display=swap">
<style>
  :root {
    --teal: #52b3a5;
    --teal-light: #7bbfb0;
    --cream: #fcf6c4;
    --arc-green: #33b36b;
    --arc-dark: #0b6b35;
    --brand-blue: #1b6fb8;
    --text-blue: #1a65a6;
    --water-top: #5e9fc0;
    --water-mid: #74cfee;
    --water-low: #6aa6dc;
    --water-deep: #5072bd;
    --white: #ffffff;
  }
  * { margin: 0; padding: 0; box-sizing: border-box; }
  html, body { width: 720px; height: 1200px; overflow: hidden; }
  body { background: var(--white); }
  .banner {
    position: relative; width: 720px; height: 1200px; overflow: hidden;
    background: linear-gradient(180deg, var(--cream) 130px, #fffef5 330px, #fdfbe8 480px);
    font-family: "Fira Sans", sans-serif;
  }
  .water { position: absolute; left: 0; top: 475px; width: 720px; height: 725px; }
  .header {
    position: absolute; left: 0; top: 0; width: 720px; height: 131px;
    background: var(--teal); border-bottom: 11px solid var(--teal-light);
  }
  .arc-title {
    position: absolute; left: 0; width: 720px; top: 6px; text-align: center;
    font-family: "Fredoka", sans-serif; font-weight: 700; font-size: 100px; line-height: 1;
    color: var(--arc-green); letter-spacing: -2px;
    -webkit-text-stroke: 12px var(--white); paint-order: stroke fill;
    filter: drop-shadow(0 0 1.5px var(--arc-dark)) drop-shadow(0 0 1.5px var(--arc-dark)) drop-shadow(0 0 1px var(--arc-dark));
  }
  .bubble-type {
    position: absolute; font-family: "Fredoka", sans-serif; font-weight: 700; line-height: 1;
    color: var(--white); -webkit-text-stroke: 7px var(--brand-blue); paint-order: stroke fill;
    filter: drop-shadow(0 0 0.5px var(--white)) drop-shadow(0 0 1px var(--white)) drop-shadow(0 0 1.5px var(--brand-blue));
  }
  .level-kicker { font-size: 34px; letter-spacing: -1px; }
  .level-name { font-size: 70px; letter-spacing: 0; }
  .section-label { font-size: 52px; letter-spacing: -1px; }
  .skills-box {
    position: absolute; border: 5px solid var(--brand-blue); border-radius: 20px;
    background: linear-gradient(180deg, rgba(232,240,220,0.6), rgba(240,246,250,0.85));
  }
  .skills-box.deep {
    border: 6px solid var(--white); border-bottom: none; border-radius: 20px 20px 0 0;
    background: linear-gradient(160deg, #a6dcf2 0%, #6fb4e0 45%, #5f95d0 100%);
  }
  .skills-list { list-style: none; position: absolute; color: var(--text-blue); font-size: 19px; line-height: 22.5px; }
  .skills-list li { position: relative; padding-left: 48px; }
  .skills-list li::before { content: "•"; position: absolute; left: 24px; font-size: 16px; }
  .deep .skills-list { color: var(--white); line-height: 23.5px; }
  .moveup-box { position: absolute; background: var(--white); border-radius: 28px; }
  .moveup-text {
    position: absolute; font-family: "Fira Sans Condensed", sans-serif; font-weight: 600;
    font-size: 20px; line-height: 22px; color: var(--text-blue); letter-spacing: -0.3px;
  }
  .avatar { position: absolute; }
  .brand-mark {
    position: absolute; left: 330px; top: 1170px; display: flex; align-items: center; gap: 5px;
    font-family: "Fira Sans", sans-serif; font-weight: 500; font-size: 14px; color: #d9e6f5; letter-spacing: 1px;
  }
  .brand-mark .square { width: 10px; height: 10px; background: #d9e6f5; }
</style>
</head>
<body>
<main class="banner">
  <svg class="water" viewBox="0 0 720 725" aria-hidden="true">
    <defs>
      <linearGradient id="waterFill" x1="0" y1="0" x2="0" y2="1">
        <stop offset="0" stop-color="var(--water-top)"/>
        <stop offset="0.25" stop-color="var(--water-mid)"/>
        <stop offset="0.55" stop-color="var(--water-low)"/>
        <stop offset="1" stop-color="var(--water-deep)"/>
      </linearGradient>
    </defs>
    <path d="M0 8 C120 2 200 32 300 30 C420 26 520 -4 610 8 C660 14 690 26 720 30 L720 725 L0 725 Z" fill="url(#waterFill)"/>
  </svg>

  <header class="header">
    <h1 class="arc-title">ARC I</h1>
  </header>

  <!-- Wader level -->
  <div class="bubble-type level-kicker" style="left:58px; top:148px;">LEVEL</div>
  <h2 class="bubble-type level-name" style="left:56px; top:186px;">WADER</h2>
  <div class="avatar" role="img" aria-label="Yellow duck avatar floating at the waterline"
       style="left:110px; top:328px; width:185px; height:220px; border-radius:45% 45% 40% 40%; background:linear-gradient(180deg,#f1ee7a 0%,#f1ee7a 60%,#5eb4c8 80%,#0aa0cc 100%);"></div>

  <section class="skills-box" style="left:358px; top:232px; width:302px; height:278px;">
    <ul class="skills-list" style="left:-5px; top:32px; width:300px;">
      <li>Gets into the water with assistance</li>
      <li>Follows pool rules</li>
      <li>Can hold big breath and get chin/ cheeks in water</li>
      <li>Cups hands to hold water and get some of face wet</li>
      <li>Doesn’t always need assistance in water</li>
    </ul>
  </section>
  <div class="bubble-type section-label" style="left:352px; top:197px;">Skills</div>

  <div class="moveup-box" style="left:358px; top:518px; width:306px; height:99px;"></div>
  <div class="bubble-type section-label" style="left:352px; top:478px;">Move-Up</div>
  <p class="moveup-text" style="left:388px; top:546px; width:250px;">Must be comfortable entering the water</p>

  <!-- Splasher level -->
  <div class="bubble-type level-kicker" style="left:58px; top:654px;">LEVEL</div>
  <h2 class="bubble-type level-name" style="left:56px; top:692px;">SPLASHER</h2>
  <div class="avatar" role="img" aria-label="Penguin avatar diving underwater"
       style="left:0; top:790px; width:330px; height:230px; border-radius:40% 50% 45% 30%; background:linear-gradient(160deg,#3f3f48 0%,#4a4a55 55%,#6f8fb8 85%,#b9d3ee 100%);"></div>

  <section class="skills-box deep" style="left:355px; top:768px; width:335px; height:277px;">
    <ul class="skills-list" style="left:-5px; top:50px; width:320px;">
      <li>Enters and exits pool without assistance</li>
      <li>Can do a slide in entry</li>
      <li>Plays in water up to chest deep</li>
      <li>Dips face and head in water</li>
      <li>Blows bubbles through the mouth</li>
    </ul>
  </section>
  <div class="bubble-type section-label" style="left:560px; top:742px;">Skills</div>

  <div class="moveup-box" style="left:192px; top:1045px; width:502px; height:77px; border-radius:34px;"></div>
  <div class="bubble-type section-label" style="left:22px; top:1058px;">Move-Up</div>
  <p class="moveup-text" style="left:240px; top:1063px; width:420px;">Must fully submerge body and head underwater (no nose holding)</p>

  <div class="brand-mark" aria-label="Walter Brightley Fieldgrounds">
    <span>WBF</span><span class="square"></span>
  </div>
</main>
</body>
</html>
```